furniture and home contents restoration

I need to list the services that we perform in our studio.
we serve the general public as well as the insurance/ remediation industry

```html
<!DOCTYPE html>
<html lang="en">
<head>
<meta charset="utf-8">
<title>Keystone Workshop – Business Card</title>
<link href="https://fonts.googleapis.com/css2?family=Source+Sans+3:wght@400;600;700&display=swap" rel="stylesheet">
<style>
  :root {
    --backdrop: #2c2d34;
    --card-dark: #1b2a33;
    --card-light: #dcdde2;
    --arc-grey: #77787e;
    --text-light: #d6d9de;
    --text-dim: #b9bec5;
    --ink: #1b2a33;
  }
  * { margin: 0; padding: 0; box-sizing: border-box; }
  html, body {
    width: 1200px; height: 1000px; overflow: hidden;
    background: var(--backdrop);
    font-family: "Source Sans 3", sans-serif;
  }
  .card {
    position: absolute; left: 220px;
    width: 760px; height: 434px;
    background: var(--card-dark);
    overflow: hidden;
  }
  .card-back { top: 48px; color: var(--text-light); padding: 26px 44px; }
  .card-front { top: 520px; }

  /* back */
  .rule { height: 1px; background: var(--text-dim); opacity: .8; }
  .headline { text-align: center; padding: 14px 0 12px; }
  .headline h2 { font-size: 18px; font-weight: 700; letter-spacing: .2px; }
  .headline p { font-size: 16px; color: var(--text-dim); margin-top: 2px; }
  .services { display: flex; justify-content: space-between; padding: 16px 0 18px; }
  .services ul { list-style: none; }
  .services li {
    font-size: 15.5px; line-height: 19.6px; color: var(--text-dim);
    display: flex; align-items: center; gap: 8px;
  }
  .services-right li { justify-content: flex-end; }
  .tick { width: 11px; height: 11px; flex: none; }
  .tagline { text-align: center; font-size: 16.5px; color: var(--text-dim); padding: 12px 0 13px; }

  /* front */
  .front-shapes { position: absolute; inset: 0; }
  .brand {
    position: absolute; left: 62px; top: 196px;
    display: flex; align-items: center; gap: 12px;
    font-family: "Source Sans 3", sans-serif; font-weight: 700;
    font-size: 38px; line-height: 40px; color: var(--ink);
    white-space: nowrap;
  }
  .brand-dot { width: 14px; height: 14px; border-radius: 50%; background: var(--ink); flex: none; }
  .contact { position: absolute; left: 492px; top: 62px; color: var(--text-light); }
  .contact .name { font-size: 20px; font-weight: 700; letter-spacing: 1px; }
  .contact address { font-style: normal; font-size: 15.5px; line-height: 19px; color: var(--text-dim); margin-top: 14px; }
  .contact ul { list-style: none; margin-top: 14px; }
  .contact li { display: flex; align-items: center; gap: 8px; font-size: 15.5px; line-height: 19px; color: var(--text-dim); }
  .contact li svg { width: 12px; height: 12px; flex: none; }
  .divider { width: 34px; height: 3px; background: var(--text-light); margin-top: 22px; }
  .specialty { font-size: 16px; font-weight: 700; margin-top: 10px; }
</style>
</head>
<body>

<section class="card card-back">
  <div class="rule"></div>
  <header class="headline">
    <h2>On-Site Inspections and Desk Review Services</h2>
    <p>Assessment Reports and Estimates for Repair and Restoration</p>
  </header>
  <div class="rule"></div>
  <div class="services">
    <ul class="services-left">
      <li><svg class="tick" viewBox="0 0 12 12"><path d="M1 6.5 4.5 10 11 2" fill="none" stroke="currentColor" stroke-width="1.6"/></svg>Antique Repair and Restoration</li>
      <li><svg class="tick" viewBox="0 0 12 12"><path d="M1 6.5 4.5 10 11 2" fill="none" stroke="currentColor" stroke-width="1.6"/></svg>Art Cleaning and Remounting</li>
      <li><svg class="tick" viewBox="0 0 12 12"><path d="M1 6.5 4.5 10 11 2" fill="none" stroke="currentColor" stroke-width="1.6"/></svg>Art and Mirror Frame Repair</li>
      <li><svg class="tick" viewBox="0 0 12 12"><path d="M1 6.5 4.5 10 11 2" fill="none" stroke="currentColor" stroke-width="1.6"/></svg>Chandelier Cleaning and Restoration</li>
      <li><svg class="tick" viewBox="0 0 12 12"><path d="M1 6.5 4.5 10 11 2" fill="none" stroke="currentColor" stroke-width="1.6"/></svg>Document Restoration</li>
      <li><svg class="tick" viewBox="0 0 12 12"><path d="M1 6.5 4.5 10 11 2" fill="none" stroke="currentColor" stroke-width="1.6"/></svg>Glass, Ceramic and Mirror Repair</li>
      <li><svg class="tick" viewBox="0 0 12 12"><path d="M1 6.5 4.5 10 11 2" fill="none" stroke="currentColor" stroke-width="1.6"/></svg>Hardware Repair and Restoration</li>
      <li><svg class="tick" viewBox="0 0 12 12"><path d="M1 6.5 4.5 10 11 2" fill="none" stroke="currentColor" stroke-width="1.6"/></svg>Kitchen Removal and Reinstallation</li>
      <li><svg class="tick" viewBox="0 0 12 12"><path d="M1 6.5 4.5 10 11 2" fill="none" stroke="currentColor" stroke-width="1.6"/></svg>Lamp Cleaning and Restoration</li>
      <li><svg class="tick" viewBox="0 0 12 12"><path d="M1 6.5 4.5 10 11 2" fill="none" stroke="currentColor" stroke-width="1.6"/></svg>Lamp Shade Replacement</li>
    </ul>
    <ul class="services-right">
      <li>Metal Polishing and Restoration<svg class="tick" viewBox="0 0 12 12"><path d="M1 6.5 4.5 10 11 2" fill="none" stroke="currentColor" stroke-width="1.6"/></svg></li>
      <li>Odor Removal and Ozone Services<svg class="tick" viewBox="0 0 12 12"><path d="M1 6.5 4.5 10 11 2" fill="none" stroke="currentColor" stroke-width="1.6"/></svg></li>
      <li>Photo Restoration<svg class="tick" viewBox="0 0 12 12"><path d="M1 6.5 4.5 10 11 2" fill="none" stroke="currentColor" stroke-width="1.6"/></svg></li>
      <li>Upholstery Cleaning and Deodorizing<svg class="tick" viewBox="0 0 12 12"><path d="M1 6.5 4.5 10 11 2" fill="none" stroke="currentColor" stroke-width="1.6"/></svg></li>
      <li>In-House Upholstery and Reupholstery<svg class="tick" viewBox="0 0 12 12"><path d="M1 6.5 4.5 10 11 2" fill="none" stroke="currentColor" stroke-width="1.6"/></svg></li>
      <li>Rug Cleaning and Restoration<svg class="tick" viewBox="0 0 12 12"><path d="M1 6.5 4.5 10 11 2" fill="none" stroke="currentColor" stroke-width="1.6"/></svg></li>
      <li>Musical Instrument Restoration<svg class="tick" viewBox="0 0 12 12"><path d="M1 6.5 4.5 10 11 2" fill="none" stroke="currentColor" stroke-width="1.6"/></svg></li>
      <li>Window Treatment Repair/ Restoration<svg class="tick" viewBox="0 0 12 12"><path d="M1 6.5 4.5 10 11 2" fill="none" stroke="currentColor" stroke-width="1.6"/></svg></li>
      <li>Leather Restoration and Replacement<svg class="tick" viewBox="0 0 12 12"><path d="M1 6.5 4.5 10 11 2" fill="none" stroke="currentColor" stroke-width="1.6"/></svg></li>
      <li>Piano Restoration and Repair<svg class="tick" viewBox="0 0 12 12"><path d="M1 6.5 4.5 10 11 2" fill="none" stroke="currentColor" stroke-width="1.6"/></svg></li>
    </ul>
  </div>
  <div class="rule"></div>
  <p class="tagline">Serving The General Public and The Insurance Industry for Over 40 Years</p>
  <div class="rule"></div>
</section>

<section class="card card-front">
  <svg class="front-shapes" viewBox="0 0 760 434" preserveAspectRatio="none" aria-hidden="true">
    <path d="M0 0 H250 C400 50 480 250 440 434 H0 Z" fill="var(--card-light)"/>
    <path d="M262 4 C425 62 508 250 468 434 H440 C480 250 400 50 250 0 Z" fill="var(--arc-grey)"/>
  </svg>
  <div class="brand"><span class="brand-dot"></span>Keystone Workshop</div>
  <div class="contact">
    <p class="name">DANIEL MARSH</p>
    <address>18 Alder Brook Rd.<br>Millbrook, NY 10599</address>
    <ul>
      <li><svg viewBox="0 0 12 12"><path d="M2.5 1 4.5 1 5.3 3.6 4 4.6C4.7 6.2 5.8 7.3 7.4 8L8.4 6.7 11 7.5V9.5C11 10.3 10.3 11 9.5 11 5 11 1 7 1 2.5 1 1.7 1.7 1 2.5 1Z" fill="currentColor"/></svg>555.204.1180</li>
      <li><svg viewBox="0 0 12 12"><rect x="3" y="0.8" width="6" height="10.4" rx="1" fill="none" stroke="currentColor" stroke-width="1.2"/><circle cx="6" cy="9.3" r=".7" fill="currentColor"/></svg>555.318.7742</li>
      <li><svg viewBox="0 0 12 12"><rect x="3" y="1" width="6" height="3" fill="currentColor"/><rect x="1" y="4.5" width="10" height="4.5" rx="1" fill="currentColor"/><rect x="3" y="8" width="6" height="3" fill="none" stroke="currentColor" stroke-width="1"/></svg>555.204.1195</li>
      <li><svg viewBox="0 0 12 12"><rect x="1" y="2.5" width="10" height="7" fill="none" stroke="currentColor" stroke-width="1.2"/><path d="M1 2.5 6 6.8 11 2.5" fill="none" stroke="currentColor" stroke-width="1.2"/></svg>dmarsh@keystonemail.com</li>
    </ul>
    <div class="divider"></div>
    <p class="specialty">Home Contents Restoration</p>
  </div>
</section>

</body>
</html>
```